Harlow Stonefield Civil Construction website design

We want a Bold website to promote our Heavy Civil Construction company, We would like an organic / tangible feel to the site. The pictures will be over saturated so they pop. We need to be able to easliy upload new projects and pictures on a regular basis.
Home page will have a full screen width image, "home page image" with silhouette and logo. It will also have about us area and picture
Page 2 will be Project Gallery with pictures in project folders
Page 3 will be an employment application form and submission
Page 4 will be Contact Us
Target Market(s)
Construction indusrty
Industry/Entity Type
Contractor
Coding
Coded - Design and coding required
Number of Pages Required
4 page
Font styles to use
Other font styles liked:
- Hypatia Sans Pro Light
Look and feel

```html
<!DOCTYPE html>
<html lang="en">
<head>
<meta charset="utf-8">
<title>Harlow Stonefield Civil Construction</title>
<link href="https://fonts.googleapis.com/css2?family=Jost:wght@300;400;500&family=Oswald:wght@400&display=swap" rel="stylesheet">
<style>
:root{
  --ink:#0b0c0f;
  --sky-top:#6f7a93;
  --sky-mid:#5a6378;
  --sky-low:#3b4150;
  --ground:#08090b;
  --paper:#e9e9e8;
  --text:#1f1f1f;
  --text-soft:#3a3a3a;
  --footer:#1b1b1b;
  --white:#ffffff;
  --social-a:#3b5998;
  --social-b:#1da1f2;
  --social-c:#0e76a8;
  --social-d:#a97a5c;
}
*{box-sizing:border-box;margin:0;padding:0}
html,body{width:1120px;height:1200px;overflow:hidden}
body{position:relative;font-family:"Jost",sans-serif;color:var(--text);background:var(--paper)}

.hero{position:absolute;left:0;top:0;width:1120px;height:642px;
  background:linear-gradient(180deg,var(--sky-top) 0%,var(--sky-mid) 45%,var(--sky-low) 85%)}
.hero-scene{position:absolute;left:0;top:360px;width:1120px;height:282px;
  background:linear-gradient(180deg,rgba(8,9,11,0) 0%,rgba(8,9,11,.55) 60%,var(--ground) 76%,var(--ground) 100%)}

.main-nav{position:absolute;left:0;top:0;width:1120px;height:68px;background:rgba(60,67,82,.85)}
.main-nav a{position:absolute;top:23px;color:var(--white);text-decoration:none;font-size:14.5px;font-weight:400;letter-spacing:.3px}
.main-nav a.active::after{content:"";position:absolute;left:2px;right:0;bottom:-6px;height:1.5px;background:var(--white)}
.main-nav a.active::before{content:"";position:absolute;left:50%;bottom:-6px;margin-left:-3px;border:3px solid transparent;border-bottom-color:var(--white);border-top:0}

.brand{position:absolute;left:237px;top:235px;height:143px}
.brand-mark{position:absolute;left:0;top:14px;width:112px;height:112px;background:var(--ink)}
.brand-rule{position:absolute;left:134px;top:0;width:2px;height:143px;background:var(--ink)}
.brand-name{position:absolute;left:156px;top:22px;white-space:nowrap;color:var(--ink);font-weight:500;line-height:1}
.brand-name .l1{display:block;font-size:46px;letter-spacing:.3px}
.brand-name .l2{display:block;font-size:27px;letter-spacing:11.5px;margin-top:14px}

.about{position:absolute;left:0;top:642px;width:1120px;height:515px;
  background:linear-gradient(135deg,#dedcd6 0%,#ecebe8 40%,#e3e0d4 65%,#efefed 100%)}
.photo{position:absolute;box-shadow:0 4px 14px rgba(0,0,0,.35)}
.photo-paving{left:132px;top:66px;width:330px;height:330px;background:linear-gradient(160deg,#3f5a3a 0%,#586a4d 45%,#8c8a82 75%,#4e4c48 100%)}
.photo-channel{left:267px;top:231px;width:222px;height:218px;background:linear-gradient(170deg,#6c8a3a 0%,#a9b57c 35%,#d8d6cc 60%,#2f3a44 100%)}
.badge{position:absolute;left:132px;top:398px;height:55px;background:var(--ink);border:5px solid var(--white);border-left:0;border-bottom:0;
  color:var(--white);font-family:"Oswald",sans-serif;font-size:15px;display:flex;align-items:center;padding:0 11px;white-space:nowrap}

.about-heading{position:absolute;left:532px;top:108px;height:58px;color:var(--ink)}
.about-heading .label{position:absolute;left:0;top:14px;font-size:27px;font-weight:400;white-space:nowrap}
.about-heading .rule{position:absolute;left:97px;top:0;width:1.5px;height:58px;background:var(--ink)}
.about-heading .name{position:absolute;left:107px;top:4px;white-space:nowrap;font-weight:400;line-height:1}
.about-heading .name .l1{display:block;font-size:26px}
.about-heading .name .l2{display:block;font-size:18px;letter-spacing:2.2px;margin-top:4px}

.lead{position:absolute;left:532px;top:184px;width:462px;font-size:13.6px;line-height:20px;font-weight:400;color:var(--text)}
.body-copy{position:absolute;left:532px;top:230px;width:462px;font-size:12.4px;line-height:20.2px;font-weight:300;color:var(--text-soft)}
.read-more{position:absolute;left:532px;top:369px;width:99px;height:37px;border:2px solid var(--ink);display:flex;align-items:center;justify-content:center;
  font-family:"Oswald",sans-serif;font-size:11.5px;color:var(--ink);text-decoration:none;text-transform:uppercase}

.site-footer{position:absolute;left:0;top:1157px;width:1120px;height:43px;background:var(--footer)}
.copyright{position:absolute;left:132px;top:13px;font-size:11.5px;color:var(--white);font-weight:300}
.social{position:absolute;left:888px;top:11px;display:flex;gap:6.5px}
.social span{width:20px;height:20px;display:block}
</style>
</head>
<body>
<header class="hero">
  <div class="hero-scene" role="img" aria-label="Silhouette of excavator, dozer and haul truck against a dusk sky"></div>
  <nav class="main-nav">
    <a class="active" href="#" style="left:335px">HOME</a>
    <a href="#" style="left:413px">PROJECT GALLERY</a>
    <a href="#" style="left:565px">EMPLOYMENT</a>
    <a href="#" style="left:695px">CONTACT US</a>
  </nav>
  <div class="brand">
    <span class="brand-mark"></span>
    <span class="brand-rule"></span>
    <h1 class="brand-name"><span class="l1">HARLOW STONEFIELD</span><span class="l2">CIVIL CONSTRUCTION</span></h1>
  </div>
</header>

<section class="about" role="img" aria-label="Faded background photo of a yellow trencher on a sandy site">
  <div class="photo photo-paving" role="img" aria-label="Curb paving machine on a wooded job site"></div>
  <div class="photo photo-channel" role="img" aria-label="Drainage channel lined with erosion control blocks"></div>
  <div class="badge">OVER 10 YEARS OF EXPERIENCE</div>

  <div class="about-heading">
    <h2 class="label">ABOUT</h2>
    <span class="rule"></span>
    <p class="name"><span class="l1">HARLOW STONEFIELD</span><span class="l2">CIVIL CONSTRUCTION</span></p>
  </div>
  <p class="lead">Lorem ipsum dolor sit amet, consectetuer adipiscing elit, sed diam nonummy nibh euismod tincidunt ut laoreet dolore magna.</p>
  <p class="body-copy">Lorem ipsum dolor sit amet, consectetuer adipiscing elit, sed diam nonummy nibh mod tincidunt ut laoreet dolore magna aliquam erat volutpat. Ut wisi enim ad minim venim, quis nostrud exerci tation ullaorper suscpit lobortis nisl ut aliquip ex ea comodo consat. Duis autem vel eum iriure dolor in hendrerit in vulputate velit esse molestie consequat, vel illum dolore eu feugiat nulla facilisis at vero eros et accumsan et iusto odio dignissim qui blandit praesent luptatum zzril delenit augue duis facilisi.</p>
  <a class="read-more" href="#">Read More</a>
</section>

<footer class="site-footer">
  <p class="copyright">Copyright © 2019 HARLOW STONEFIELD. All Rights Reserved.</p>
  <div class="social">
    <span style="background:var(--social-a)"></span>
    <span style="background:var(--social-b)"></span>
    <span style="background:var(--social-c)"></span>
    <span style="background:var(--social-d)"></span>
  </div>
</footer>
</body>
</html>
```